Clean energy startup needs brochure & datasheet

• We are a solar energy start-up providing solar hybrid solutions for off-grid power demand. We need a brochure for our flagship product: our modular, transportable solar power generator, which can be installed in addition to diesel generators or batteries.
• Please visit our website www.voltarine.com to get a better feel for what we do.
• The goal of this brochure is to explain how our solar generator works and that Voltarine provides 2 different types of systems (solar-diesel and solar-battery), according to the customer needs.
• Size of the brochure (each page) is A4
• It will mostly be sent by email, so all pages should look good even if the viewer can see only one page (no graphics spanning several pages)
• A key challenge is the very high density of information on our pages - the color scheme should help in separating the main points and highlight the main conclusions
Updates

Project Deadline Extended
Reason: We still have multiple designs under consideration and need more time to work out the details.

Project Deadline Extended
Reason: We are getting close ! We were quite late in giving feedback last week, sorry for that. Thus, we give you some more time to finalise your job. Good luck !

Target Market(s)

Potential customers, meaning people all the way from diesel technicians to executives working in various sectors (prime markets are mining, light industry, construction, utilities, real estate,…)

Industry/Entity Type

Solar Energy

Font styles to use
Serif
Sans Serif

Requirements
Must have
• • Design a clean, easy to read, 4 page-brochure (A4 format bifold) with general explanations of the systems (see attached file 6 for the content and some layout ideas)
• Design one inlay datasheet (A4 double sided) with some specific technical specs of the various equipment sizes, to added in the brochure (see attached file 6 for the content and some layout ideas)
• Use Voltarine logo and derive a color scheme from our logos (there are several versions in orange, gray and white, allowing a choice of potential color schemes)
• Designers should propose multiple backgrounds for our solar generator pictures (the files with solar racking with a currently transparent background), e.g. Middle East (Desert) / Africa (Savannah) / Afghanistan (Mountains)
• Ability to edit raw files in Adobe Illustrator / Photoshop (please check with us if you want to use another program)

Nice to have
• • Provision to change pictures later (as we get real pictures from our demo plants)
Should not have
• • Any images or allusions to wind power, biomass, or other forms of renewable energy that are not solar
• Any images or allusions to green European looking landscapes (lawns, green trees, etc.) - this is a product for the Middle East & Africa!
• Any images or allusions to people in suits - this is an industrial product

```html
<!DOCTYPE html>
<html lang="en">
<head>
<meta charset="utf-8">
<title>Voltarine – Solar Generator Datasheet</title>
<link href="https://fonts.googleapis.com/css2?family=Arimo:ital,wght@0,400;0,700;1,700&display=swap" rel="stylesheet">
<style>
:root{
  --backdrop:#ece9e4;
  --paper:#ffffff;
  --ink:#222222;
  --muted:#555555;
  --orange:#f0a04b;
  --sun:#f7b500;
  --charcoal:#1d1d1d;
  --heat-zero:#4caf50;
  --heat-low:#f3df6a;
  --heat-mid:#f5a65b;
  --heat-high:#e5534b;
  --sky-top:#3f7fd0;
  --sky-low:#b7d6f2;
  --roof:#5d6063;
}
*{box-sizing:border-box;margin:0;padding:0}
html,body{width:1200px;height:864px;overflow:hidden;background:var(--backdrop);font-family:"Arimo",Arial,sans-serif;color:var(--ink)}
.spread{position:absolute;left:25px;top:25px;width:1150px;height:815px;display:flex;box-shadow:0 2px 10px rgba(0,0,0,.25)}
.page-left{position:relative;width:575px;height:100%;background:var(--paper)}
.page-right{position:relative;width:575px;height:100%;overflow:hidden}

.section-title{position:absolute;left:0;width:575px;text-align:center;font-weight:700;font-style:italic;font-size:17px}
.title-config{top:24px}
.title-daily{top:416px}

.spec-table{position:absolute;left:37px;top:59px;width:499px;border-collapse:collapse;font-size:9.5px}
.spec-table td{border:1px solid var(--orange);text-align:center;padding:1px 4px;line-height:11px}
.spec-table td.label{text-align:left;width:148px}
.spec-table td.indent{padding-left:10px}

.notes{position:absolute;left:130px;top:325px;font-size:10.5px;line-height:13px;list-style:none}
.notes li{position:relative;padding-left:14px;margin-bottom:4px}
.notes li::before{content:"";position:absolute;left:0;top:5px;width:4px;height:4px;border-radius:50%;background:var(--ink)}

.block-caption{position:absolute;left:34px;top:452px;font-size:11px}
.heat-unit{position:absolute;left:32px;top:473px;font-size:5px;color:var(--muted)}
.heat-table{position:absolute;left:32px;top:480px;width:510px;border-collapse:collapse;font-size:5px;table-layout:fixed}
.heat-table th,.heat-table td{border:1px solid #555;height:15px;text-align:center;font-weight:400;background:var(--heat-zero);color:#1a1a1a}
.heat-table thead th{background:#fff}
.heat-table thead th.corner{background:var(--heat-high);text-align:left;padding-left:2px}
.heat-table th.month{background:#fff;text-align:left;padding-left:2px;width:31px}
.heat-table td.y{background:var(--heat-low)}
.heat-table td.o{background:var(--heat-mid)}
.heat-table td.r{background:var(--heat-high)}
.heat-table .total{background:#fff;width:38px}
.heat-table tfoot td{background:#fff}
.heat-table tfoot td.blank{border:none}

.footer-rule{position:absolute;left:0;top:706px;width:575px;height:3px;background:#cfcfcf}
.footer-brand{position:absolute;left:34px;top:735px}
.brand-name{font-weight:700;font-size:28px;color:var(--sun);display:flex;align-items:center;gap:7px}
.brand-dot{width:16px;height:16px;border-radius:50%;background:var(--sun)}
.brand-tagline{font-size:10px;color:var(--muted);margin-top:2px;padding-left:23px}
.contact{position:absolute;left:252px;top:733px;font-size:14px;line-height:18px}
.contact strong{font-style:italic;font-size:15px}

.photo{position:absolute;inset:0;background:linear-gradient(180deg,var(--sky-top) 0%,var(--sky-low) 45%,#9aa3ab 46%,var(--roof) 70%,#8a8d90 100%)}
.swoosh{position:absolute;left:0;top:0}
.cover-brand{position:absolute;left:335px;top:662px}
.cover-brand .brand-name{font-size:36px}
.cover-brand .brand-tagline{color:#fff;font-size:12px;padding-left:28px}
.cover-lines{position:absolute;right:23px;top:759px;text-align:right;color:#fff;font-size:13px;line-height:18px}
</style>
</head>
<body>
<div class="spread">
  <section class="page-left">
    <h2 class="section-title title-config">Solar Generator configuration options</h2>
    <table class="spec-table">
      <tr><td class="label"></td><td>Single block</td><td>Full 20' container</td><td>Full 40' container</td></tr>
      <tr><td class="label">Solar generator capacity (kWp<sub>DC</sub>)<sup>1)</sup></td><td>24</td><td>72</td><td>168</td></tr>
      <tr><td class="label">Peak output (kW<sub>AC</sub> / kVA)</td><td>20</td><td>60</td><td>140</td></tr>
      <tr><td class="label">Avg. energy generation <sup>2)</sup></td><td></td><td></td><td></td></tr>
      <tr><td class="label indent">Daily min. (kWh<sub>AC</sub> / day)</td><td>96</td><td>288</td><td>672</td></tr>
      <tr><td class="label indent">Daily max. (kWh<sub>AC</sub> / day)</td><td>120</td><td>360</td><td>840</td></tr>
      <tr><td class="label indent">Annually min. (kWh<sub>AC</sub> / year)</td><td>35'040</td><td>105'120</td><td>245'280</td></tr>
      <tr><td class="label indent">Annually max. (kWh<sub>AC</sub> / year)</td><td>43'800</td><td>131'400</td><td>306'600</td></tr>
      <tr><td class="label">Module area (m2)</td><td>158</td><td>475</td><td>1'109</td></tr>
      <tr><td class="label">Layout options <sup>3)</sup></td><td>50m x 4m (single row) /<br>25m x 12m (double row)</td><td>75m x 12 m (double row) /<br>50m x 20m (triple row)</td><td>75m x 36m (5 rows) /<br>50m x 52m (7 rows)</td></tr>
      <tr><td class="label">&nbsp;</td><td></td><td></td><td></td></tr>
      <tr><td class="label">Recommended minimum diesel generator capacity (kVA)</td><td>~50</td><td>~100</td><td>~250</td></tr>
      <tr><td class="label">Battery capacity</td><td colspan="3">up to 24h (on request)</td></tr>
    </table>
    <ul class="notes">
      <li>Other capacities are available in multiples of 24 kWp</li>
      <li>Typical range up to 30° latitude. Actual output depends<br>on the exact location</li>
      <li>Other layouts available on request</li>
    </ul>

    <h2 class="section-title title-daily">Typical energy generation during the day</h2>
    <p class="block-caption">Standard 24 kWp Solar Generator block</p>
    <p class="heat-unit">Solar kWh</p>
    <table class="heat-table">
      <thead><tr><th class="corner month">Time</th><th>00:00</th><th>01:00</th><th>02:00</th><th>03:00</th><th>04:00</th><th>05:00</th><th>06:00</th><th>07:00</th><th>08:00</th><th>09:00</th><th>10:00</th><th>11:00</th><th>12:00</th><th>13:00</th><th>14:00</th><th>15:00</th><th>16:00</th><th>17:00</th><th>18:00</th><th>19:00</th><th>20:00</th><th>21:00</th><th>22:00</th><th>23:00</th><th class="total">Monthly Total</th></tr></thead>
      <tbody>
        <tr><th class="month">January</th><td>0.0</td><td>0.0</td><td>0.0</td><td>0.0</td><td>0.0</td><td>0.0</td><td>0.0</td><td>0.0</td><td class="y">0.9</td><td class="y">4.1</td><td class="o">8.0</td><td class="o">11.7</td><td class="r">13.8</td><td class="r">15.5</td><td class="r">14.4</td><td class="o">11.7</td><td class="o">8.7</td><td class="y">4.6</td><td class="y">1.2</td><td>0.0</td><td>0.0</td><td>0.0</td><td>0.0</td><td>0.0</td><td class="total">2'931</td></tr>
        <tr><th class="month">February</th><td>0.0</td><td>0.0</td><td>0.0</td><td>0.0</td><td>0.0</td><td>0.0</td><td>0.0</td><td>0.0</td><td class="y">1.7</td><td class="o">6.2</td><td class="o">10.6</td><td class="r">14.1</td><td class="r">16.3</td><td class="r">17.2</td><td class="r">16.2</td><td class="r">13.9</td><td class="o">10.4</td><td class="o">5.9</td><td class="y">1.7</td><td>0.0</td><td>0.0</td><td>0.0</td><td>0.0</td><td>0.0</td><td class="total">3'196</td></tr>
        <tr><th class="month">March</th><td>0.0</td><td>0.0</td><td>0.0</td><td>0.0</td><td>0.0</td><td>0.0</td><td>0.0</td><td class="y">0.2</td><td class="y">2.9</td><td class="o">7.4</td><td class="o">11.3</td><td class="r">14.3</td><td class="r">16.2</td><td class="r">16.9</td><td class="r">15.6</td><td class="r">13.8</td><td class="o">10.8</td><td class="o">6.6</td><td class="y">2.3</td><td>0.0</td><td>0.0</td><td>0.0</td><td>0.0</td><td>0.0</td><td class="total">3'665</td></tr>
        <tr><th class="month">April</th><td>0.0</td><td>0.0</td><td>0.0</td><td>0.0</td><td>0.0</td><td>0.0</td><td>0.0</td><td class="y">1.3</td><td class="o">5.1</td><td class="o">9.1</td><td class="r">12.8</td><td class="r">16.2</td><td class="r">17.8</td><td class="r">18.3</td><td class="r">17.7</td><td class="r">15.8</td><td class="r">12.2</td><td class="o">7.9</td><td class="y">3.4</td><td class="y">0.3</td><td>0.0</td><td>0.0</td><td>0.0</td><td>0.0</td><td class="total">4'130</td></tr>
        <tr><th class="month">May</th><td>0.0</td><td>0.0</td><td>0.0</td><td>0.0</td><td>0.0</td><td>0.0</td><td>0.0</td><td class="y">2.3</td><td class="o">6.3</td><td class="o">10.4</td><td class="r">13.6</td><td class="r">15.9</td><td class="r">17.4</td><td class="r">17.9</td><td class="r">17.0</td><td class="r">15.2</td><td class="r">12.3</td><td class="o">8.4</td><td class="y">4.1</td><td class="y">0.7</td><td>0.0</td><td>0.0</td><td>0.0</td><td>0.0</td><td class="total">4'390</td></tr>
        <tr><th class="month">June</th><td>0.0</td><td>0.0</td><td>0.0</td><td>0.0</td><td>0.0</td><td>0.0</td><td class="y">0.2</td><td class="y">2.4</td><td class="o">6.0</td><td class="o">9.6</td><td class="r">12.3</td><td class="r">14.4</td><td class="r">15.8</td><td class="r">16.3</td><td class="r">15.8</td><td class="r">14.1</td><td class="o">11.5</td><td class="o">8.0</td><td class="y">4.3</td><td class="y">1.1</td><td>0.0</td><td>0.0</td><td>0.0</td><td>0.0</td><td class="total">3'958</td></tr>
        <tr><th class="month">July</th><td>0.0</td><td>0.0</td><td>0.0</td><td>0.0</td><td>0.0</td><td>0.0</td><td>0.0</td><td class="y">1.6</td><td class="y">4.8</td><td class="o">8.4</td><td class="o">11.6</td><td class="r">14.5</td><td class="r">16.0</td><td class="r">16.4</td><td class="r">16.0</td><td class="r">14.2</td><td class="o">11.3</td><td class="o">7.7</td><td class="y">4.0</td><td class="y">1.0</td><td>0.0</td><td>0.0</td><td>0.0</td><td>0.0</td><td class="total">3'953</td></tr>
        <tr><th class="month">August</th><td>0.0</td><td>0.0</td><td>0.0</td><td>0.0</td><td>0.0</td><td>0.0</td><td>0.0</td><td class="y">1.2</td><td class="y">4.7</td><td class="o">8.7</td><td class="r">12.2</td><td class="r">14.8</td><td class="r">16.5</td><td class="r">17.0</td><td class="r">16.2</td><td class="r">14.1</td><td class="o">11.3</td><td class="o">7.5</td><td class="y">3.4</td><td class="y">0.6</td><td>0.0</td><td>0.0</td><td>0.0</td><td>0.0</td><td class="total">3'977</td></tr>
        <tr><th class="month">September</th><td>0.0</td><td>0.0</td><td>0.0</td><td>0.0</td><td>0.0</td><td>0.0</td><td>0.0</td><td class="y">0.9</td><td class="y">4.6</td><td class="o">9.0</td><td class="r">12.7</td><td class="r">15.4</td><td class="r">16.9</td><td class="r">17.2</td><td class="r">16.3</td><td class="r">14.1</td><td class="o">10.9</td><td class="o">6.7</td><td class="y">2.2</td><td>0.0</td><td>0.0</td><td>0.0</td><td>0.0</td><td>0.0</td><td class="total">3'808</td></tr>
        <tr><th class="month">October</th><td>0.0</td><td>0.0</td><td>0.0</td><td>0.0</td><td>0.0</td><td>0.0</td><td>0.0</td><td class="y">0.8</td><td class="y">3.9</td><td class="o">8.4</td><td class="r">12.1</td><td class="r">14.9</td><td class="r">16.4</td><td class="r">16.4</td><td class="r">15.3</td><td class="r">12.8</td><td class="o">8.9</td><td class="y">4.3</td><td class="y">0.9</td><td>0.0</td><td>0.0</td><td>0.0</td><td>0.0</td><td>0.0</td><td class="total">3'455</td></tr>
        <tr><th class="month">November</th><td>0.0</td><td>0.0</td><td>0.0</td><td>0.0</td><td>0.0</td><td>0.0</td><td>0.0</td><td>0.0</td><td class="y">2.8</td><td class="o">7.1</td><td class="o">10.8</td><td class="r">13.5</td><td class="r">15.3</td><td class="r">15.2</td><td class="r">14.0</td><td class="o">11.7</td><td class="o">7.8</td><td class="y">3.1</td><td class="y">0.1</td><td>0.0</td><td>0.0</td><td>0.0</td><td>0.0</td><td>0.0</td><td class="total">3'042</td></tr>
        <tr><th class="month">December</th><td>0.0</td><td>0.0</td><td>0.0</td><td>0.0</td><td>0.0</td><td>0.0</td><td>0.0</td><td>0.0</td><td class="y">1.6</td><td class="o">5.1</td><td class="o">8.9</td><td class="o">11.4</td><td class="r">12.6</td><td class="r">12.7</td><td class="r">12.0</td><td class="o">10.1</td><td class="o">6.6</td><td class="y">2.5</td><td>0.0</td><td>0.0</td><td>0.0</td><td>0.0</td><td>0.0</td><td>0.0</td><td class="total">2'591</td></tr>
      </tbody>
      <tfoot><tr><td class="blank" colspan="22"></td><td colspan="2">Yearly Total</td><td class="total">43'096</td></tr></tfoot>
    </table>

    <div class="footer-rule"></div>
    <div class="footer-brand">
      <div class="brand-name"><span class="brand-dot"></span>Voltarine</div>
      <div class="brand-tagline">Clean Power. Off the Grid.</div>
    </div>
    <div class="contact">
      <strong>For more information, Contact us at</strong><br>
      Contact Us : +971 4 555 0192<br>
      Log On : www.voltarine.com or
    </div>
  </section>

  <section class="page-right">
    <div class="photo" role="img" aria-label="Photo of a tiled house roof fitted with solar panels against a bright blue sky"></div>
    <svg class="swoosh" width="575" height="815" viewBox="0 0 575 815">
      <path d="M0 650 C150 605 350 578 575 580 L575 815 L0 815 Z" fill="#ffffff"/>
      <path d="M0 680 C160 625 360 598 575 594 L575 815 L0 815 Z" fill="var(--sun)"/>
      <path d="M0 745 C170 665 370 622 575 614 L575 815 L0 815 Z" fill="var(--charcoal)"/>
    </svg>
    <div class="cover-brand">
      <div class="brand-name"><span class="brand-dot"></span>Voltarine</div>
      <div class="brand-tagline">Clean Power. Off the Grid.</div>
    </div>
    <div class="cover-lines">
      Voltarine solar hybrid systems<br>
      Cheaper and cleaner energy than diesel generators
    </div>
  </section>
</div>
</body>
</html>
```